Kestrel Cove Camp

We need a web page that details location/distance to Melbourne, the facilities available, the magnificent setting, contact information, history of the area and our background in the industry booking enquiry page linked to our email account, feedback page.
(Refer www.campbrindlepoint.com.au for details and further imagary as we operate in the same facility and Camp Brindle Point Business no longer exists) WE WANT A BETTER WEBSITE THAN THIS!!

```html
<!DOCTYPE html>
<html lang="en">
<head>
<meta charset="utf-8">
<title>Kestrel Cove Camp</title>
<link href="https://fonts.googleapis.com/css2?family=Arimo:wght@400;700&family=Open+Sans:wght@400;600&display=swap" rel="stylesheet">
<style>
:root{
  --topbar:#1c1d21;
  --topbar-text:#8893a4;
  --topbar-link:#6d86a8;
  --nav-text:#ffffff;
  --panel:rgba(40,44,40,.78);
  --panel-dark:rgba(30,34,36,.82);
  --head-top:#5b6178;
  --head-bottom:#3a3f56;
  --button:#1f7fae;
  --footer:#11141f;
  --footer-head:#8a93a6;
  --footer-link:#747d90;
  --box:#1b1f2f;
  --bottom:#050608;
  --accent:#f08a1c;
}
*{margin:0;padding:0;box-sizing:border-box}
html,body{width:1049px;height:1200px;overflow:hidden;background:var(--bottom)}
body{position:relative;font-family:Arimo,Arial,sans-serif}
.abs{position:absolute}
.topbar{left:0;top:0;width:1049px;height:50px;background:linear-gradient(#2a2b30,#111215);}
.subscribe{left:67px;top:18px;font:11px "Open Sans",sans-serif;color:var(--topbar-text);letter-spacing:.5px}
.subscribe a{color:var(--topbar-link);text-decoration:none}
.subscribe span{margin:0 7px;color:#555}
.top-icon{top:17px;width:15px;height:15px;border-radius:3px}
.search{left:790px;top:10px;width:185px;height:27px;border-radius:7px;background:#0c0c0e;color:#444a55;font:10px "Open Sans",sans-serif;letter-spacing:1px;padding:7px 10px}
.scenery{left:0;top:50px;width:1049px;height:878px;background:linear-gradient(110deg,#2d5f8a 0%,#3b6e8c 25%,#52624a 45%,#3e5233 70%,#4d6a3e 100%)}
.brand{left:67px;top:68px;display:flex;align-items:center;gap:10px;font:700 22px Arimo,Arial,sans-serif;color:var(--accent)}
.brand i{width:44px;height:44px;border-radius:50%;background:var(--accent);display:block}
.nav{top:95px;font:700 17px Arimo,Arial,sans-serif;color:var(--nav-text);text-shadow:0 1px 2px rgba(0,0,0,.6)}
.slide{left:68px;top:153px;width:907px;height:324px;background:linear-gradient(#7e9ccc 0%,#a7bfdc 33%,#3a8bb0 38%,#cbbfa5 48%,#d8ccb1 70%,#5d6d3a 100%)}
.dot{top:487px;width:13px;height:13px;border-radius:50%;background:#3d4a63}
.dot.on{background:#2f9ad4}
.content{left:69px;top:519px;width:906px;height:390px;background:var(--panel)}
.col-head{top:538px;width:275px;height:44px;background:linear-gradient(var(--head-top),var(--head-bottom));color:#fff;font:700 19px Arimo,Arial,sans-serif;display:flex;align-items:center;padding-left:14px;gap:12px}
.col-head svg{flex:none}
.map{left:90px;top:581px;width:274px;height:225px;background:linear-gradient(135deg,#7fa6c2,#4f8fbf 60%,#3a78b0);border:1px solid #cfd8e2}
.fb-photo{left:404px;top:601px;width:237px;height:82px;background:linear-gradient(#9bc0e6 0%,#5f8a46 40%,#2bb6c9 62%,#e9e3d2 100%)}
.fb-title{left:384px;top:700px;width:310px;text-align:center;color:#fff;font:700 17px Arimo,Arial,sans-serif}
.contact{left:679px;top:582px;width:276px;height:221px;background:var(--panel-dark)}
.c-icon{left:703px;width:29px;height:29px;border-radius:6px}
.c-label{left:741px;color:#fff;font:700 13px Arimo,Arial,sans-serif}
.social{left:679px;top:814px;width:276px;height:76px;background:var(--panel-dark)}
.s-icon{top:838px;width:29px;height:29px;border-radius:6px;background:#7c8aa2}
.btn{top:833px;height:38px;background:var(--button);color:#fff;font:700 12px Arimo,Arial,sans-serif;display:flex;align-items:center;justify-content:center}
.comments{left:415px;top:846px;color:#fff;font:700 12px Arimo,Arial,sans-serif}
.footer{left:0;top:928px;width:1049px;height:213px;background:var(--footer)}
.f-head{top:957px;color:var(--footer-head);font:700 21px Arimo,Arial,sans-serif}
.f-links{left:69px;top:1003px;list-style:none;font:12px "Open Sans",sans-serif;color:var(--footer-link);letter-spacing:.5px;line-height:19px}
.thumb{width:51px;height:51px;border:3px solid #1e2232;}
.updates{left:680px;top:999px;width:291px;height:111px;background:var(--box);border-radius:8px}
.updates-tail{left:944px;top:984px}
.bottom{left:0;top:1141px;width:1049px;height:59px;background:var(--bottom);border-top:1px solid #1a1d26}
.copy{left:64px;top:1164px;font:11px "Open Sans",sans-serif;color:#8a93a6;letter-spacing:.5px}
.legal{right:78px;top:1164px;font:11px "Open Sans",sans-serif;color:#7e93b3;letter-spacing:.5px}
.legal span{color:#555c6b;margin:0 7px}
</style>
</head>
<body>
<div class="abs topbar"></div>
<div class="abs subscribe">Subscribe to: <a>Posts</a><span>|</span><a>Comments</a><span>|</span><a>Email</a></div>
<div class="abs top-icon" style="left:715px;background:#e87a1e"></div>
<div class="abs top-icon" style="left:740px;background:#4566a8"></div>
<div class="abs top-icon" style="left:765px;background:#49b6dd"></div>
<div class="abs search">Search Keywords</div>

<div class="abs scenery" role="img" aria-label="Aerial photograph of the coastline, bay and farmland around the camp"></div>
<div class="abs brand"><i></i>Kestrel Cove Camp</div>
<div class="abs nav" style="left:467px">Home</div>
<div class="abs nav" style="left:553px">Accommdation</div>
<div class="abs nav" style="left:695px">Activities</div>
<div class="abs nav" style="left:791px">Menu</div>
<div class="abs nav" style="left:860px">Private Camps</div>

<div class="abs slide" role="img" aria-label="Photograph of a long sandy beach with grassy dunes and distant hills"></div>
<div class="abs dot on" style="left:477px"></div>
<div class="abs dot" style="left:496px"></div>
<div class="abs dot" style="left:515px"></div>
<div class="abs dot" style="left:534px"></div>
<div class="abs dot" style="left:553px"></div>

<div class="abs content"></div>

<div class="abs col-head" style="left:90px">
  <svg width="24" height="22" viewBox="0 0 24 22"><circle cx="12" cy="6" r="5" fill="#9aa3ba"/><path d="M2 22c0-7 4-9 10-9s10 2 10 9z" fill="#9aa3ba"/></svg>Location</div>
<div class="abs col-head" style="left:384px">
  <svg width="26" height="24" viewBox="0 0 26 24"><path d="M3 2h14a2 2 0 0 1 2 2v8a2 2 0 0 1-2 2H9l-5 4v-4H3a2 2 0 0 1-2-2V4a2 2 0 0 1 2-2z" fill="#9aa3ba"/><circle cx="19" cy="17" r="6" fill="#7c86a0"/></svg>FeedBack</div>
<div class="abs col-head" style="left:679px">
  <svg width="24" height="24" viewBox="0 0 24 24"><path d="M5 2l4 5-2 3c1 3 4 6 7 7l3-2 5 4-3 4C10 22 2 14 1 5z" fill="#9aa3ba"/></svg>Get In Touch</div>

<div class="abs map" role="img" aria-label="Locality map showing the drive from Melbourne to the camp"></div>

<div class="abs fb-photo" role="img" aria-label="Photograph of a tropical beach with palm trees"></div>
<div class="abs fb-title">MY feedback</div>

<div class="abs contact"></div>
<svg class="abs c-icon" style="top:607px" viewBox="0 0 29 29"><rect width="29" height="29" rx="6" fill="#2f8fd6"/><path d="M9 6l3 4-2 2c1 3 3 5 6 6l2-2 4 3-2 4C13 23 6 16 6 9z" fill="#fff"/></svg>
<div class="abs c-label" style="top:605px">PHONE</div>
<svg class="abs c-icon" style="top:655px" viewBox="0 0 29 29"><rect x="1" y="6" width="27" height="19" rx="2" fill="#e8e8e8"/><path d="M2 7l12.5 10L27 7" fill="none" stroke="#aaa" stroke-width="1.5"/></svg>
<div class="abs c-label" style="top:654px">EMAIL</div>
<svg class="abs c-icon" style="top:704px" viewBox="0 0 29 29"><circle cx="14.5" cy="14.5" r="13" fill="#22a5e3"/></svg>
<div class="abs c-label" style="top:703px">SKYPE</div>
<svg class="abs c-icon" style="top:753px" viewBox="0 0 29 29"><circle cx="14.5" cy="14.5" r="13" fill="#22a5e3"/></svg>
<div class="abs c-label" style="top:751px">OTHER REQUEST</div>

<div class="abs social"></div>
<div class="abs s-icon" style="left:703px"></div>
<div class="abs s-icon" style="left:742px"></div>
<div class="abs s-icon" style="left:781px"></div>
<div class="abs s-icon" style="left:820px"></div>
<div class="abs s-icon" style="left:859px"></div>
<div class="abs s-icon" style="left:898px"></div>

<div class="abs btn" style="left:110px;width:85px">Learn More</div>
<div class="abs comments">23 Comments</div>
<div class="abs btn" style="left:511px;width:83px">Read More</div>

<div class="abs footer"></div>
<div class="abs f-head" style="left:70px">About Us</div>
<div class="abs f-head" style="left:215px">History</div>
<div class="abs f-head" style="left:446px">The Gallery</div>
<div class="abs f-head" style="left:695px">Updates</div>
<ul class="abs f-links">
  <li>Our Company</li><li>Our Blog</li><li>Submit a Site</li><li>Contact Us</li><li>Help &amp; Terms</li><li>Read Our FAQ</li>
</ul>
<div class="abs thumb" style="left:395px;top:1004px;background:linear-gradient(#3b7cc6,#e5dcc6)" role="img" aria-label="Gallery photo of a beach umbrella"></div>
<div class="abs thumb" style="left:456px;top:1004px;background:linear-gradient(#4cc3d6,#2b8fb0)" role="img" aria-label="Gallery photo of turquoise water"></div>
<div class="abs thumb" style="left:517px;top:1004px;background:linear-gradient(#9ed1e6,#f1f1ef)" role="img" aria-label="Gallery photo of white sand"></div>
<div class="abs thumb" style="left:578px;top:1004px;background:linear-gradient(#7aa9c9,#4a6a58)" role="img" aria-label="Gallery photo of a bay"></div>
<div class="abs thumb" style="left:395px;top:1062px;background:linear-gradient(#2f6fa6,#3a5b3a)" role="img" aria-label="Gallery photo of cliffs"></div>
<div class="abs thumb" style="left:456px;top:1062px;background:linear-gradient(#1d6f9c,#58b8d0)" role="img" aria-label="Gallery photo of a lagoon"></div>
<div class="abs thumb" style="left:517px;top:1062px;background:linear-gradient(#a9cfe0,#c7a86c)" role="img" aria-label="Gallery photo of palm trees"></div>
<div class="abs thumb" style="left:578px;top:1062px;background:linear-gradient(#6fb4dc,#eef2f3)" role="img" aria-label="Gallery photo of a shoreline"></div>
<svg class="abs updates-tail" width="22" height="18" viewBox="0 0 22 18"><path d="M0 0L22 18H0z" fill="var(--box)"/></svg>
<div class="abs updates"></div>

<div class="abs bottom"></div>
<div class="abs copy">© 2010 Copyright Harbourline Theme. All Rights Reserved.</div>
<div class="abs legal">Log in<span>|</span>Privacy Policy<span>|</span>Terms and Conditions<span>|</span>Contact Us<span>|</span>Back to Top</div>
</body>
</html>
```